Residential and Commercial Roofing Specialists
Quality - Service - Trust - Knowledge
Project: Residential and Commercial Roofing Specialists
Industry: Construction
Residential and Commercial Roofing Specialists - Construction
Creative Brief
I need single sided standard sized Business Card [3.5" x 2"]
Use any fonts similar that matches well with the logo.
Professional
Milo Penfield
Owner
4620 W. 31st Lane
Unit 2397
Scottsdale, AZ 85390
mpenfieldroofing@tarvolmail.com
www.mpenfieldroofing-example.com
Brellin Certified Inspector #07458316

```html
<!DOCTYPE html>
<html lang="en">
<head>
<meta charset="utf-8">
<title>Penfield Construction Stationery</title>
<link rel="stylesheet" href="https://fonts.googleapis.com/css2?family=Source+Sans+3:wght@300;400;600;700&display=swap">
<style>
:root{
  --ink:#1a1a1a;
  --navy:#13315c;
  --blue:#1f5f93;
  --steel:#2b6fa3;
  --grey-panel:#e6e6e6;
  --grey-label:#d4d4d4;
  --text-soft:#555;
  --paper:#ffffff;
  --backdrop:#d9d9d9;
  --faint:#e9eef3;
}
*{box-sizing:border-box;margin:0;padding:0}
html,body{width:1200px;height:564px;overflow:hidden}
body{background:var(--backdrop);font-family:"Source Sans 3",Arial,sans-serif;color:var(--ink);position:relative}
.sheet{position:absolute;background:var(--paper);overflow:hidden;box-shadow:0 1px 4px rgba(0,0,0,.25)}
.brand{position:absolute;display:flex;align-items:center;gap:5px;white-space:nowrap}
.brand-square{width:12px;height:12px;background:var(--blue);flex:none}
.brand-name{font-weight:700;color:var(--blue);line-height:1;text-transform:uppercase;letter-spacing:.5px}
.band{position:absolute;left:0;right:0;bottom:0;height:16px;border-top:2px solid var(--ink);background:var(--paper)}
.band-bar{position:absolute;left:0;right:0;bottom:0;height:12px;background:linear-gradient(90deg,var(--blue),var(--navy));color:#fff;font-size:6.4px;font-weight:600;letter-spacing:2.2px;text-align:center;line-height:12px;white-space:nowrap}

/* envelope */
.envelope-front{left:33px;top:26px;width:392px;height:174px}
.envelope-front .brand{left:18px;top:22px}
.envelope-front .brand-name{font-size:15px}
.envelope-address{position:absolute;left:18px;top:66px;font-size:5.6px}
.envelope-back{left:106px;top:217px;width:332px;height:174px;border:1px solid #bbb}
.envelope-back svg{position:absolute;left:0;top:0}
.envelope-back .brand{left:140px;top:24px}
.envelope-back .brand-name{font-size:11px}

/* cards */
.card{top:428px;width:191px;height:109px;border-radius:4px}
.card-one{left:33px}
.card-two{left:231px}
.card .brand{left:0;right:0;top:14px;justify-content:center}
.card .brand-name{font-size:13px}
.card-tagline{position:absolute;left:0;right:0;text-align:center;font-size:5.4px;font-weight:600;white-space:nowrap}
.card-one .card-tagline{top:46px}
.card-two .card-tagline{top:51px;height:10px;line-height:10px;background:var(--ink);color:#fff;letter-spacing:.4px}
.card-base{position:absolute;left:0;right:0;bottom:0;background:linear-gradient(90deg,var(--steel),var(--navy));color:#fff}
.card-one .card-base{top:56px;border-top:2px solid var(--ink)}
.card-two .card-base{top:61px}
.card-person{position:absolute;left:8px;top:8px;width:80px;text-align:right}
.card-name{font-size:8.5px;font-weight:700;letter-spacing:.2px;text-transform:uppercase}
.card-role{font-size:6px;font-weight:300;letter-spacing:.6px}
.card-cert{position:absolute;left:6px;bottom:9px;font-size:3.9px;white-space:nowrap}
.card-divider{position:absolute;left:95px;top:8px;bottom:8px;width:1px;background:rgba(255,255,255,.6)}
.card-contact{position:absolute;left:100px;top:7px;font-size:4.3px;line-height:5.8px;white-space:nowrap}
.card-contact p.gap{margin-top:2px}
.card-contact b{font-weight:700}

/* letterhead & fax */
.letterhead{left:438px;top:26px;width:361px;height:510px}
.fax{left:805px;top:26px;width:361px;height:510px}
.letterhead .brand,.fax .brand{left:18px;top:24px}
.letterhead .brand-name,.fax .brand-name{font-size:15px}
.sender{position:absolute;left:270px;top:27px;font-size:4.3px;line-height:5.7px;white-space:nowrap}
.sender b{font-weight:700}
.watermark{position:absolute;left:10px;right:10px;top:440px;display:flex;justify-content:center;align-items:center;gap:7px;white-space:nowrap}
.watermark-square{width:20px;height:20px;background:var(--faint);flex:none}
.watermark-name{font-size:21px;line-height:1;font-weight:700;color:var(--faint);text-transform:uppercase;letter-spacing:1px}
.letter{position:absolute;left:33px;top:110px;width:295px;font-size:6.9px;line-height:8.6px;color:var(--text-soft);font-weight:400}
.letter p{margin-bottom:8.6px}
.letter .salutation{margin-top:13px}
.letter .closing{margin-top:24px}
.signature{position:absolute;left:100px;top:402px;width:72px;height:32px;background:linear-gradient(90deg,rgba(40,70,170,.15),rgba(40,70,170,.3));border-radius:3px}

.fax-title{position:absolute;right:28px;top:80px;font-size:13px;line-height:1;font-weight:300;letter-spacing:1px}
.fax-panel{position:absolute;left:0;right:0;top:98px;height:76px;background:var(--grey-panel)}
.fax-row{position:absolute;left:32px;display:flex;gap:2px;height:15px}
.fax-label{background:var(--grey-label);font-size:6px;line-height:15px;padding-left:5px}
.fax-label.short{width:36px}
.fax-field{background:#fff;width:108px}
.fax-field.wide{width:109px;margin-right:1px}
.fax-options{position:absolute;left:32px;top:181px;display:flex;gap:16px;font-size:6px;color:var(--text-soft);white-space:nowrap}
.fax-options span{display:flex;align-items:center;gap:4px}
.fax-options i{width:6px;height:6px;border:1px solid #333;display:inline-block}
.fax-comments{position:absolute;left:32px;top:204px;font-size:6px;color:var(--text-soft)}
</style>
</head>
<body>

<section class="sheet envelope-front">
  <div class="brand"><span class="brand-square"></span><span class="brand-name">Penfield Construction</span></div>
  <p class="envelope-address">4620 W. 31st Lane, Unit 2397, Scottsdale, AZ 85390</p>
  <div class="band"><div class="band-bar">Your residential and commercial roofing specialists.</div></div>
</section>

<section class="sheet envelope-back">
  <svg width="332" height="174" viewBox="0 0 332 174" aria-hidden="true">
    <path d="M0 0 C2 16 14 22 40 30 L172 66 C190 72 210 72 228 66 L332 36" fill="none" stroke="#333" stroke-width=".7"/>
  </svg>
  <div class="brand"><span class="brand-square" style="width:9px;height:9px"></span><span class="brand-name">Penfield Construction</span></div>
</section>

<section class="sheet card card-one">
  <div class="brand"><span class="brand-square"></span><span class="brand-name">Penfield Construction</span></div>
  <p class="card-tagline">Your residential and commercial roofing specialists.</p>
  <div class="card-base">
    <div class="card-person"><p class="card-name">Milo Penfield</p><p class="card-role">OWNER</p></div>
    <p class="card-cert">Brellin Certified Inspector #07458316</p>
    <span class="card-divider"></span>
    <div class="card-contact">
      <p>4620 W. 31st Lane</p><p>Unit 2397, Scottsdale, AZ 85390</p>
      <p class="gap"><b>Phone</b> : 303-555-0148</p>
      <p><b>Email</b> : mpenfieldroofing@tarvolmail.com</p>
      <p><b>Web</b> : www.mpenfieldroofing-example.com</p>
    </div>
  </div>
</section>

<section class="sheet card card-two">
  <div class="brand"><span class="brand-square"></span><span class="brand-name">Penfield Construction</span></div>
  <p class="card-tagline">Your residential and commercial roofing specialists.</p>
  <div class="card-base">
    <div class="card-person"><p class="card-name">Milo Penfield</p><p class="card-role">OWNER</p></div>
    <p class="card-cert">Brellin Certified Inspector #07458316</p>
    <span class="card-divider"></span>
    <div class="card-contact">
      <p>4620 W. 31st Lane</p><p>Unit 2397, Scottsdale, AZ 85390</p>
      <p class="gap"><b>Phone</b> : 303-555-0148</p>
      <p><b>Email</b> : mpenfieldroofing@tarvolmail.com</p>
      <p><b>Web</b> : www.mpenfieldroofing-example.com</p>
    </div>
  </div>
</section>

<section class="sheet letterhead">
  <div class="brand"><span class="brand-square"></span><span class="brand-name">Penfield Construction</span></div>
  <div class="sender">
    <p>4620 W. 31st Lane</p><p>Unit 2397, Scottsdale, AZ 85390</p>
    <p><b>Phone:</b> 303-555-0148</p><p>www.mpenfieldroofing-example.com</p>
    <p>Brellin Certified Inspector #07458316</p>
  </div>
  <div class="watermark"><span class="watermark-square"></span><span class="watermark-name">Penfield Construction</span></div>
  <div class="letter">
    <p>Someone Some body<br>100 Long St<br>Brisbane, Australia</p>
    <p class="salutation">Dear Someone Somebody,</p>
    <p>Lorem ipsum dolor sit amet, consectetuer adipiscing elit, sed diam nonummy nibh euismod tincidunt ut laoreet dolore magna aliquam erat volutpat. Ut wisi enim ad minim veniam, quis nostrud exerci tation ullamcorper suscipit lobortis nisl ut aliquip ex ea commodo consequat. Duis autem vel eum iriure dolor in hendrerit in vulputate velit esse molestie consequat, vel illum dolore eu feugiat nulla facilisis at vero eros et accumsan et iusto odio dignissim qui blandit praesent luptatum zzril delenit augue duis dolore te feugait nulla facilisi.</p>
    <p>Lorem ipsum dolor sit amet, consectetuer adipiscing elit, sed diam nonummy nibh euismod tincidunt ut laoreet dolore magna aliquam erat volutpat. Ut wisi enim ad minim veniam, quis nostrud exerci tation ullamcorper suscipit lobortis nisl ut aliquip ex ea commodo consequat. Duis autem vel eum iriure dolor in hendrerit in vulputate velit esse molestie consequat, vel illum dolore eu feugiat nulla facilisis at vero eros et accumsan et iusto odio dignissim qui blandit praesent luptatum zzril delenit augue duis dolore te feugait nulla facilisi.</p>
    <p>Lorem ipsum dolor sit amet, consectetuer adipiscing elit, sed diam nonummy nibh euismod tincidunt ut laoreet dolore magna aliquam erat volutpat. Ut wisi enim ad minim veniam, quis nostrud exerci tation ullamcorper suscipit lobortis nisl ut aliquip ex ea commodo consequat. Duis autem vel eum iriure dolor in hendrerit in vulputate velit esse molestie consequat, vel illum dolore eu feugiat nulla facilisis at vero eros et accumsan et iusto odio dignissim qui blandit praesent luptatum zzril delenit augue duis dolore te feugait nulla facilisi.</p>
    <p class="closing">Youre Sincerely.<br>Owen Tarrick.</p>
  </div>
  <div class="signature" role="img" aria-label="Handwritten signature in blue ink"></div>
  <div class="band"><div class="band-bar">Your residential and commercial roofing specialists.</div></div>
</section>

<section class="sheet fax">
  <div class="brand"><span class="brand-square"></span><span class="brand-name">Penfield Construction</span></div>
  <div class="sender">
    <p>4620 W. 31st Lane</p><p>Unit 2397, Scottsdale, AZ 85390</p>
    <p><b>Phone:</b> 303-555-0148</p><p>www.mpenfieldroofing-example.com</p>
    <p>Brellin Certified Inspector #07458316</p>
  </div>
  <p class="fax-title">FAX</p>
  <div class="fax-panel"></div>
  <div class="fax-row" style="top:102px"><span class="fax-label short">To:</span><span class="fax-field wide"></span><span class="fax-label short">From:</span><span class="fax-field"></span></div>
  <div class="fax-row" style="top:120px"><span class="fax-label short">Fax:</span><span class="fax-field wide"></span><span class="fax-label short">Pages:</span><span class="fax-field"></span></div>
  <div class="fax-row" style="top:138px"><span class="fax-label short">Phone:</span><span class="fax-field wide"></span><span class="fax-label short">Date:</span><span class="fax-field"></span></div>
  <div class="fax-row" style="top:156px"><span class="fax-label short">Re:</span><span class="fax-field wide"></span><span class="fax-label short">CC:</span><span class="fax-field"></span></div>
  <div class="fax-options">
    <span><i></i>Urgent</span><span><i></i>For Review</span><span><i></i>Please Comment</span><span><i></i>Please Reply</span><span><i></i>Please Recycle</span>
  </div>
  <p class="fax-comments">Comments:</p>
  <div class="watermark"><span class="watermark-square"></span><span class="watermark-name">Penfield Construction</span></div>
  <div class="band"><div class="band-bar">Your residential and commercial roofing specialists.</div></div>
</section>

</body>
</html>
```